Facebook ad design for Velvetloomtrinkets

Design 6 x FB ads for online jewellery store (South Africa) selling bracelets, charms and rings. Use high quality images which do not have any copyright restrictions. Please advise regarding optimal size for high FB ads. (1080 x 1080 pixels?) The logo of the business is attached in uploaded file. It is not necessary to use the logo on ads. The ads must look professional and clear. Additional text will be added on the ads by the owner. Do not stick to color scheme of the site or FB page. So do not use the pink. The main requirement is that the ads must look very professional. The website will also be redesigned.
https://velvetloomtrinkets.example/
https://www.facebook.com/VelvetloomTrinkets.example
The ads must specifically be designed for and target the following days.
1 for mother's day
1 for valentine's day
1 for Christmas
1 with love theme
2 general to target female jewellery lovers (bracelets / charms)

Alternatively you can create 10 images for FB carousel ad (1080 x 1080 pixels) with products from the actual website. Use high quality images from the web, but use products that is listed on the Velvetloomtrinkets website. Use your imagination. Simple, modern and elegant.

Target Market(s)

Ladies / Woman

Font styles to use
Sans Serif

Colors

Designer to choose colors to be used in the design.

Requirements
Nice to have
• Professional / Modern / Elegant ads

```html
<!DOCTYPE html>
<html lang="en">
<head>
<meta charset="UTF-8">
<title>Velvetloomtrinkets – Mother's Day</title>
<link rel="stylesheet" href="https://fonts.googleapis.com/css2?family=Cinzel:wght@400;500&family=Great+Vibes&display=swap">
<style>
  :root {
    --crimson: #d8103b;
    --crimson-deep: #b90a30;
    --ink: #141414;
    --paper: #ffffff;
    --rose-soft: #f6d3d6;
    --rose-peach: #f8e1cf;
    --leaf: #dfe6d4;
    --silver-light: #f1f2f4;
    --silver-mid: #b9bcc2;
    --skin-glow: #e9a1ad;
  }
  html, body {
    margin: 0;
    padding: 0;
    width: 1200px;
    height: 1200px;
    overflow: hidden;
    background: var(--paper);
  }
  .ad {
    position: relative;
    width: 1200px;
    height: 1200px;
    overflow: hidden;
    background: var(--paper);
    font-family: "Cinzel", "Times New Roman", serif;
  }
  .ad h1, .ad p { margin: 0; font-weight: 400; }
  .rose-bouquet {
    position: absolute;
    left: 444px;
    top: 0;
    width: 756px;
    height: 430px;
    background:
      radial-gradient(ellipse 40% 45% at 70% 30%, var(--rose-soft) 0%, rgba(246,211,214,0) 70%),
      radial-gradient(ellipse 35% 40% at 35% 25%, var(--rose-peach) 0%, rgba(248,225,207,0) 70%),
      radial-gradient(ellipse 50% 45% at 85% 70%, var(--rose-soft) 0%, rgba(246,211,214,0) 75%),
      radial-gradient(ellipse 30% 30% at 20% 55%, var(--leaf) 0%, rgba(223,230,212,0) 70%);
  }
  .brand {
    position: absolute;
    left: 61px;
    top: 128px;
    width: 376px;
    text-align: center;
    font-weight: 500;
    font-size: 28px;
    letter-spacing: 0.5px;
    color: var(--ink);
  }
  .headline-top {
    position: absolute;
    left: 0;
    width: 1210px;
    top: 345px;
    text-align: center;
    font-size: 96px;
    line-height: 1;
    color: var(--crimson);
    letter-spacing: 2px;
  }
  .mom-letter {
    position: absolute;
    top: 488px;
    font-size: 340px;
    line-height: 1;
    color: var(--crimson);
  }
  .mom-letter.first { left: 140px; }
  .mom-letter.last { left: 736px; }
  .ring-photo {
    position: absolute;
    left: 453px;
    top: 452px;
    width: 288px;
    height: 324px;
    border-radius: 48% 48% 50% 50%;
    background: radial-gradient(ellipse at 50% 40%, var(--silver-light) 0%, var(--silver-mid) 100%);
  }
  .celebration-band {
    position: absolute;
    left: 0;
    top: 822px;
    width: 1200px;
    height: 378px;
    background: var(--crimson);
  }
  .family-photo {
    position: absolute;
    right: 0;
    top: 0;
    width: 311px;
    height: 378px;
    background:
      radial-gradient(ellipse 70% 60% at 75% 40%, var(--skin-glow) 0%, rgba(233,161,173,0) 75%),
      linear-gradient(90deg, rgba(216,16,59,0) 0%, var(--crimson-deep) 100%);
  }
  .celebrating {
    position: absolute;
    left: 0;
    width: 1250px;
    top: 880px;
    text-align: center;
    font-size: 94px;
    line-height: 1;
    color: var(--paper);
    letter-spacing: 1px;
  }
  .occasion {
    position: absolute;
    left: 0;
    width: 1160px;
    top: 980px;
    text-align: center;
    font-family: "Great Vibes", "Brush Script MT", cursive;
    font-size: 168px;
    line-height: 1.1;
    color: var(--paper);
  }
</style>
</head>
<body>
  <main class="ad">
    <div class="rose-bouquet" role="img" aria-label="Bouquet of soft pink and peach roses"></div>

    <div class="brand">Velvetloomtrinkets</div>

    <h1 class="headline-top">I LOVE YOU</h1>

    <span class="mom-letter first">M</span>
    <div class="ring-photo" role="img" aria-label="Silver three-stone diamond ring standing upright, forming the letter O"></div>
    <span class="mom-letter last">M</span>

    <section class="celebration-band">
      <div class="family-photo" role="img" aria-label="Mother holding her baby, tinted red"></div>
    </section>

    <p class="celebrating">CELEBRATING</p>
    <p class="occasion">Mother’s Day!</p>
  </main>
</body>
</html>
```